Postcards for Upscale Landscaping Company
Harbor Fern KT
Postcards for Upscale Landscaping Company  - Home and Garden
Creative Brief
Home and Garden
High end homeowners in the $2m+ range. Owner specializing in fine gardening and hedge/topiary trimming.
Need a design for a 5x7 postcard. Front with stamp will just include the logo and and mission statement, name, contact info etc. as on current business card to be submitted.
Tbrantley Tbrantley
I’m not sure we have the card in that file format. I’ll work on it and get Bach to you. Thanks.
sarvesh sarvesh
Hi, Please upload your logo in Ai or PNG file format.

```html
<!DOCTYPE html>
<html lang="en">
<head>
<meta charset="utf-8">
<title>Harbor Fern KT — Postcard</title>
<link rel="stylesheet" href="https://fonts.googleapis.com/css2?family=EB+Garamond:wght@400&family=Lato:wght@300;400;700&display=swap">
<style>
  :root {
    --paper: #ffffff;
    --ink: #111111;
    --brand-red: #b0464a;
    --band-text: #fbeeee;
    --rule: #222222;
    --hydrangea-deep: #2f56c4;
    --hydrangea-mid: #5a86e6;
    --hydrangea-light: #a9c3f4;
    --leaf: #3d6a3a;
    --window-white: #f2f4f8;
  }
  * { margin: 0; padding: 0; box-sizing: border-box; }
  html, body { width: 1200px; height: 869px; overflow: hidden; background: var(--paper); }
  .postcard {
    position: relative;
    width: 1200px;
    height: 869px;
    background: var(--paper);
    overflow: hidden;
  }
  .garden-photo {
    position: absolute;
    left: 0; top: 0;
    width: 516px; height: 869px;
    background:
      radial-gradient(ellipse 140px 120px at 370px 140px, var(--window-white) 0%, rgba(242,244,248,0) 100%),
      radial-gradient(ellipse 200px 160px at 140px 380px, var(--hydrangea-mid) 0%, rgba(90,134,230,0) 100%),
      radial-gradient(ellipse 170px 150px at 360px 440px, var(--leaf) 0%, rgba(61,106,58,0) 100%),
      radial-gradient(ellipse 260px 220px at 220px 700px, var(--hydrangea-light) 0%, rgba(169,195,244,0) 100%),
      linear-gradient(180deg, #e7ecf3 0%, var(--hydrangea-mid) 30%, var(--hydrangea-deep) 65%, var(--hydrangea-mid) 100%);
  }
  .brand {
    position: absolute;
    left: 516px; right: 0;
    top: 244px;
    display: flex;
    align-items: center;
    justify-content: center;
    gap: 14px;
  }
  .brand-dot {
    width: 20px; height: 20px;
    border-radius: 50%;
    background: var(--brand-red);
  }
  .brand-name {
    font-family: "Lato", sans-serif;
    font-weight: 400;
    font-size: 34px;
    line-height: 44px;
    color: var(--ink);
  }
  .headline {
    position: absolute;
    left: 588px;
    top: 318px;
    font-family: "EB Garamond", serif;
    font-weight: 400;
    font-size: 45px;
    line-height: 66px;
    color: var(--ink);
  }
  .experience-band {
    position: absolute;
    left: 516px; right: 0;
    top: 458px; height: 122px;
    background: var(--brand-red);
    display: flex;
    flex-direction: column;
    justify-content: center;
    align-items: center;
    font-family: "Lato", sans-serif;
    font-weight: 300;
    font-size: 20px;
    line-height: 38px;
    color: var(--band-text);
    text-align: center;
  }
  .contact {
    position: absolute;
    left: 557px;
    top: 630px;
    font-family: "Lato", sans-serif;
    color: var(--ink);
  }
  .contact-name { font-weight: 700; font-size: 28px; line-height: 36px; }
  .contact-role { font-weight: 700; font-size: 22px; line-height: 30px; }
  .contact-details {
    margin-top: 24px;
    font-weight: 400;
    font-size: 19px;
    line-height: 31px;
  }
  .address-lines {
    position: absolute;
    left: 902px;
    top: 678px;
    width: 262px;
  }
  .address-line {
    height: 2px;
    background: var(--rule);
    margin-bottom: 22px;
  }
  .address-line.short { width: 73%; }
</style>
</head>
<body>
  <main class="postcard">
    <div class="garden-photo" role="img" aria-label="Photograph of blue hydrangea blooms with green leaves beside a white window frame"></div>

    <div class="brand">
      <span class="brand-dot"></span>
      <span class="brand-name">Harbor Fern KT</span>
    </div>

    <h1 class="headline">Full Service Landscape &amp;<br>Property Management</h1>

    <div class="experience-band">
      <p>15 Years of Experience specializing in Fine Gardening</p>
      <p>And Hedge/Topiary Trimming</p>
    </div>

    <section class="contact">
      <p class="contact-name">Tom Brantley</p>
      <p class="contact-role">Owner</p>
      <div class="contact-details">
        <p>555 014-2290</p>
        <p>www.harborferngardens.com</p>
        <p>tom@harborferngardens.com</p>
      </div>
    </section>

    <div class="address-lines" aria-hidden="true">
      <div class="address-line"></div>
      <div class="address-line"></div>
      <div class="address-line"></div>
      <div class="address-line"></div>
      <div class="address-line short"></div>
    </div>
  </main>
</body>
</html>
```